Equipment Finance Specialist I work with companies who need the funds to buy their equipment

I would like a business card that stands out on the shelves. I want to be able to hand it to someone and say WOW. This card should have my logo.
You can put color into it I am very open on design and color

What my company does is we deal with dealerships that sell equipment such as Dump Trucks garbage trucks tractors trailers. Customers get referred to us and depending on their time in business we will ask for the following items

Companies that have been in business for more than two years we have a credit application program up to 250K . With this program we need the following items Credit application filled out(which is what I would like to be able for the customer to click on my website to get.) as well as three current month bank statements.

Deals over 250k we will need the following items

2 years business tax returns
2 years personal tax returns
Profit & Loss statement
Personal Financial Statement

what we do
100% FINANCING
SEASONAL PAYMENTS
LOAN BALLOON PAYMENTS
TRAC LEASING
LOW-INTEREST REFINANCING RATES
DEBT CONSOLIDATION

We specialize in creative financing solutions and offer a variety of reliable, flexible and expandable lending choices.

Target Market(s)

Trucking Companies

Industry/Entity Type

Trucking Company

Contact Information for Business Card

* $250,000 Application only Program
* Loans from $30,000 to 5,000,000
* Competitive Interest Rates

Font styles to use
Serif
Sans Serif

Colors

Designer to choose colors to be used in the design.

Requirements
Must have
• On the back of the card.
• * $250,000 Application only Program
• * Loans from $30,000 to 5,000,000
• My name, email, website. address
• * Competitive Interest Rates
• * 100% Financing
Nice to have
• I want my logo to pop on the card
• My logo is the great one I would like to use
Should not have
• I am up for your creativity as well

```html
<!DOCTYPE html>
<html lang="en">
<head>
<meta charset="utf-8">
<title>Summit Lending – Business Card</title>
<link rel="stylesheet" href="https://fonts.googleapis.com/css2?family=Saira:wght@300;400;700&display=swap">
<style>
  :root {
    --stage: #2b2d30;
    --card-black: #0b0b0c;
    --card-red: #d91c2a;
    --navy: #233a8c;
    --white: #ffffff;
    --soft-white: #e4e4e4;
    --accent-red: #e0202e;
    --emblem: #2a2a2c;
  }
  * { margin: 0; padding: 0; box-sizing: border-box; }
  html, body { width: 1200px; height: 900px; overflow: hidden; }
  body {
    background: var(--stage);
    font-family: "Saira", Arial, sans-serif;
    position: relative;
  }
  .card {
    position: absolute;
    width: 560px;
    height: 320px;
    border-radius: 22px;
    overflow: hidden;
  }

  /* Front card */
  .card-front { left: 110px; top: 90px; background: var(--card-black); color: var(--soft-white); }
  .logo-panel {
    position: absolute;
    left: -250px; top: -70px;
    width: 460px; height: 460px;
    border-radius: 50%;
    background: var(--white);
    border: 18px solid var(--navy);
  }
  .brand {
    position: absolute;
    left: 22px; top: 118px;
    display: flex; align-items: center; gap: 8px;
    color: var(--navy);
    font-weight: 700;
    font-size: 26px;
    line-height: 1;
    text-transform: uppercase;
  }
  .brand-dot { width: 18px; height: 18px; border-radius: 50%; background: var(--navy); flex: none; }
  .brand-name { display: flex; flex-direction: column; letter-spacing: 0.5px; }
  .emblem {
    position: absolute;
    left: 290px; top: 60px;
    width: 230px; height: 230px;
    border-radius: 50%;
    background: radial-gradient(circle, #333336 0%, var(--emblem) 70%, #1c1c1e 100%);
  }
  .contact {
    position: absolute;
    display: flex; gap: 10px; align-items: flex-start;
    font-weight: 300; font-size: 14px; line-height: 1.45;
  }
  .contact svg { flex: none; margin-top: 3px; }
  .contact-phone { left: 232px; top: 28px; }
  .contact-web { left: 232px; top: 92px; }
  .contact-address { left: 232px; top: 240px; }
  .person {
    position: absolute;
    right: 30px; top: 150px;
    text-align: right;
  }
  .person-name { font-weight: 700; font-size: 28px; color: var(--white); letter-spacing: 0.5px; line-height: 1.1; }
  .person-name .surname { color: var(--accent-red); }
  .person-role { font-weight: 400; font-size: 14px; color: var(--white); margin-top: 2px; }

  /* Back card */
  .card-back { left: 530px; top: 490px; background: var(--card-red); }
  .back-brand {
    position: absolute;
    left: 70px; top: 60px;
    display: flex; align-items: center; gap: 14px;
    color: var(--navy);
    font-weight: 700; font-size: 44px; line-height: 1;
    text-transform: uppercase;
  }
  .back-brand .brand-dot { width: 30px; height: 30px; }
  .offer-list {
    position: absolute;
    left: 74px; top: 170px;
    list-style: none;
    color: var(--white);
    font-weight: 400; font-size: 17px; line-height: 1.35;
  }
  .offer-list li::before { content: "*"; }
</style>
</head>
<body>

<section class="card card-front" aria-label="Business card front">
  <div class="logo-panel"></div>
  <div class="brand">
    <span class="brand-dot"></span>
    <span class="brand-name"><span>Summit</span><span>Lending</span></span>
  </div>

  <div class="emblem" role="img" aria-label="Large faint truck illustration inside a circle"></div>

  <div class="contact contact-phone">
    <svg width="14" height="14" viewBox="0 0 24 24" aria-hidden="true">
      <path fill="#e0202e" d="M6.6 10.8a15 15 0 0 0 6.6 6.6l2.2-2.2a1 1 0 0 1 1-.25 11.4 11.4 0 0 0 3.6.57 1 1 0 0 1 1 1V20a1 1 0 0 1-1 1A17 17 0 0 1 3 4a1 1 0 0 1 1-1h3.5a1 1 0 0 1 1 1c0 1.25.2 2.45.57 3.6a1 1 0 0 1-.25 1z"/>
    </svg>
    <div>+64 (0)9 555 0142<br>021 555 018</div>
  </div>

  <div class="contact contact-web">
    <svg width="14" height="14" viewBox="0 0 24 24" aria-hidden="true">
      <circle cx="12" cy="12" r="10" fill="#e0202e"/>
      <path d="M2 12h20M12 2c3 3 3 17 0 20M12 2c-3 3-3 17 0 20" stroke="#0b0b0c" stroke-width="1.5" fill="none"/>
    </svg>
    <div>info@summitlending.co<br>www.summitlending.co</div>
  </div>

  <div class="contact contact-address">
    <svg width="14" height="16" viewBox="0 0 24 28" aria-hidden="true">
      <path fill="#e0202e" d="M12 0a10 10 0 0 0-10 10c0 7.5 10 18 10 18s10-10.5 10-18A10 10 0 0 0 12 0z"/>
      <circle cx="12" cy="10" r="4" fill="#0b0b0c"/>
    </svg>
    <div>48 Harbour View Lane,<br>Ellerslie, Auckland 1051, NZ</div>
  </div>

  <div class="person">
    <div class="person-name">Marcus <span class="surname">Hale</span></div>
    <div class="person-role">Founder | CEO</div>
  </div>
</section>

<section class="card card-back" aria-label="Business card back">
  <div class="back-brand">
    <span class="brand-dot"></span>
    <span>Summit Lending</span>
  </div>
  <ul class="offer-list">
    <li>$250,000 Application only Program</li>
    <li>Loans from $30,000 to 5,000,000</li>
    <li>Competitive Interest Rates</li>
    <li>100% Financing</li>
  </ul>
</section>

</body>
</html>
```